Plakat-Design für Zimmerei
Zielgruppe
Wir sind eine Zimmerei traditionell geprägte Zimmerei, die ihr Hauptaugenmerk auf Qualität und Zuverlässigkeit legt. Zur Zeit umfasst die Zimmerei Holger Brandt neben dem Inhaber zwei weitere Zimmerergesellen, einen Auszubildenden und einen Praktikanten.
Unsere Zielgruppe sind alle Personen- und Unternehmensgruppen in der nahen Umgebung, welche Zimmererarbeiten in Anspruch nehmen wollen.
Aufgabenstellung
Unsere Plakatwerbung soll vor allem Einfach und Übersichtlich gehalten werden.
Folgende Infos sollen dargestellt werden:
Zimmerei Holger Brandt
Aus dem Banner soll erstellt werden:
Baugerüstplanen: 200 cm x 205 cm
Bauzaunbanner: 340 cm x 173 cm
Schilder: 70 cm x 100 cm

```html
<!DOCTYPE html>
<html lang="de">
<head>
<meta charset="utf-8">
<title>Zimmerei Holger Brandt – Werbemittel</title>
<link href="https://fonts.googleapis.com/css2?family=Roboto:wght@500;700&family=Roboto+Slab:wght@700;800&display=swap" rel="stylesheet">
<style>
:root{
  --brown:#6b4425;
  --brown-dark:#5a3719;
  --tan:#f1c98c;
  --tan-shadow:#3f2510;
  --wood-light:#f6dfba;
  --wood-mid:#eecf9f;
  --label:#7a4e2a;
  --illus:#cfa574;
  --white:#ffffff;
}
*{margin:0;padding:0;box-sizing:border-box}
html,body{width:981px;height:1200px;overflow:hidden;background:var(--white)}
body{position:relative;font-family:"Roboto",Arial,sans-serif}
.label{position:absolute;font-family:"Roboto",Arial,sans-serif;font-weight:700;color:var(--label);font-size:19px;transform:translateX(-50%);white-space:nowrap}
.piece{position:absolute;overflow:hidden;background:linear-gradient(100deg,var(--wood-light) 0%,var(--wood-mid) 35%,var(--wood-light) 60%,var(--wood-mid) 100%)}
.band{position:absolute;left:0;right:0;background:var(--brown)}
.brush{position:absolute;background:var(--brown-dark);border-radius:4px 10px 6px 12px}
.headline{position:absolute;left:0;right:0;text-align:center;font-family:"Roboto Slab",Georgia,serif;font-weight:800;color:var(--tan);line-height:1;white-space:nowrap;text-shadow:2px 3px 0 var(--tan-shadow)}
.owner{position:absolute;left:0;right:0;text-align:center;font-family:"Roboto Slab",Georgia,serif;font-weight:700;color:var(--tan);white-space:nowrap;line-height:1}
.web{position:absolute;left:0;right:0;text-align:center;font-family:"Roboto Slab",Georgia,serif;font-weight:700;color:var(--tan);white-space:nowrap;line-height:1}
.contact{position:absolute;display:flex;align-items:center;color:var(--brown);font-weight:500;white-space:nowrap;line-height:1}
.contact svg{fill:var(--brown);flex:none}
.mark{position:absolute;border-radius:50%;background:var(--white);border:2px solid #222;display:flex;align-items:center;justify-content:center;font-family:"Roboto Slab",Georgia,serif;font-weight:700;color:var(--brown)}
.illustration{position:absolute;background:linear-gradient(160deg,rgba(207,165,116,.55),rgba(160,115,70,.35));border-radius:4px}
</style>
</head>
<body>
<svg width="0" height="0" style="position:absolute">
  <symbol id="i-pin" viewBox="0 0 24 24"><path d="M12 1a8 8 0 0 0-8 8c0 6 8 14 8 14s8-8 8-14a8 8 0 0 0-8-8zm0 11a3 3 0 1 1 0-6 3 3 0 0 1 0 6z"/></symbol>
  <symbol id="i-phone" viewBox="0 0 24 24"><path d="M6.6 2.5l3 3.4-1.8 2.6c1.3 3 3.6 5.4 6.6 6.8l2.5-1.9 3.5 3-1.8 3.4C10 19.5 4.2 13.7 3.9 4.4z"/></symbol>
  <symbol id="i-mobile" viewBox="0 0 24 24"><path d="M8 1h8a2 2 0 0 1 2 2v18a2 2 0 0 1-2 2H8a2 2 0 0 1-2-2V3a2 2 0 0 1 2-2zm0 3v14h8V4zm4 15.5a1 1 0 1 0 0 2 1 1 0 0 0 0-2z" transform="rotate(-25 12 12)"/></symbol>
  <symbol id="i-mail" viewBox="0 0 24 24"><path d="M1 5h22v14H1zm2 2v.5l9 6 9-6V7l-9 6z"/></symbol>
</svg>

<!-- Baugerüstplane -->
<div class="label" style="left:296px;top:40px">Baugerüstplane</div>
<section class="piece scaffold-tarp" style="left:60px;top:87px;width:493px;height:505px">
  <div class="band" style="top:33px;height:228px"></div>
  <div class="mark" style="left:192px;top:12px;width:110px;height:110px;font-size:20px">Brandt</div>
  <div class="headline" style="top:130px;font-size:70px">ZIMMEREI</div>
  <div class="headline" style="top:202px;font-size:45px">HOLGER BRANDT</div>
  <div class="brush" style="left:64px;top:256px;width:376px;height:40px"></div>
  <div class="owner" style="top:267px;font-size:18px">Inh. Holger Brandt | Zimmerermeister</div>
  <div class="illustration" role="img" aria-label="Skizze eines Holz-Dachstuhls" style="left:318px;top:338px;width:170px;height:120px"></div>
  <div class="contact" style="left:20px;top:310px;font-size:21px"><svg width="22" height="22"><use href="#i-pin"/></svg><span style="margin-left:12px">Lindenhofweg 12 • 56070 Musterstadt</span></div>
  <div class="contact" style="left:20px;top:350px;font-size:23px"><svg width="22" height="22"><use href="#i-phone"/></svg><span style="margin-left:12px">0261 / 58320</span></div>
  <div class="contact" style="left:20px;top:384px;font-size:23px"><svg width="22" height="22"><use href="#i-mobile"/></svg><span style="margin-left:12px">0171 / 4409213</span></div>
  <div class="contact" style="left:20px;top:420px;font-size:21px"><svg width="22" height="22"><use href="#i-mail"/></svg><span style="margin-left:12px">info@zimmerei-brandt.de</span></div>
  <div class="brush" style="left:6px;top:455px;width:482px;height:46px"></div>
  <div class="web" style="top:465px;font-size:28px">www.zimmerei-brandt.de</div>
</section>

<!-- Schild -->
<div class="label" style="left:765px;top:175px">Schild</div>
<section class="piece sign" style="left:636px;top:225px;width:257px;height:367px">
  <div class="band" style="top:28px;height:138px"></div>
  <div class="mark" style="left:95px;top:12px;width:68px;height:68px;font-size:13px">Brandt</div>
  <div class="headline" style="top:86px;font-size:37px;text-shadow:1px 2px 0 var(--tan-shadow)">ZIMMEREI</div>
  <div class="headline" style="top:122px;font-size:23px;text-shadow:1px 2px 0 var(--tan-shadow)">HOLGER BRANDT</div>
  <div class="brush" style="left:16px;top:152px;width:224px;height:24px"></div>
  <div class="owner" style="top:159px;font-size:11px">Inh. Holger Brandt | Zimmerermeister</div>
  <div class="illustration" role="img" aria-label="Skizze eines Holz-Dachstuhls" style="left:100px;top:245px;width:145px;height:85px"></div>
  <div class="contact" style="left:10px;top:186px;font-size:11px"><svg width="12" height="12"><use href="#i-pin"/></svg><span style="margin-left:6px">Lindenhofweg 12 • 56070 Musterstadt</span></div>
  <div class="contact" style="left:10px;top:205px;font-size:11px"><svg width="12" height="12"><use href="#i-phone"/></svg><span style="margin-left:6px">0261 / 58320</span></div>
  <div class="contact" style="left:10px;top:222px;font-size:11px"><svg width="12" height="12"><use href="#i-mobile"/></svg><span style="margin-left:6px">0171 / 4409213</span></div>
  <div class="contact" style="left:10px;top:239px;font-size:11px"><svg width="12" height="12"><use href="#i-mail"/></svg><span style="margin-left:6px">info@zimmerei-brandt.de</span></div>
  <div class="brush" style="left:4px;top:336px;width:249px;height:28px"></div>
  <div class="web" style="top:342px;font-size:16px">www.zimmerei-brandt.de</div>
</section>

<!-- Bauzaunbanner -->
<div class="label" style="left:242px;top:641px">Bauzaunbanner</div>
<section class="piece fence-banner" style="left:21px;top:674px;width:942px;height:478px">
  <div class="band" style="top:0;height:152px"></div>
  <div class="headline" style="top:26px;font-size:60px;text-shadow:3px 4px 0 var(--tan-shadow)">ZIMMEREI HOLGER BRANDT</div>
  <div class="brush" style="left:163px;top:102px;width:600px;height:58px"></div>
  <div class="owner" style="top:113px;font-size:28px;left:-50px">Inh. Holger Brandt | Zimmerermeister</div>
  <div class="mark" style="left:772px;top:96px;width:128px;height:128px;font-size:24px">Brandt</div>
  <div class="illustration" role="img" aria-label="Skizze eines Holz-Dachstuhls" style="left:565px;top:210px;width:345px;height:190px"></div>
  <div class="contact" style="left:38px;top:178px;font-size:34px"><svg width="34" height="34"><use href="#i-pin"/></svg><span style="margin-left:14px">Lindenhofweg 12 • 56070 Musterstadt</span></div>
  <div class="contact" style="left:38px;top:243px;font-size:37px"><svg width="34" height="34"><use href="#i-phone"/></svg><span style="margin-left:14px">0261 / 58320</span></div>
  <div class="contact" style="left:38px;top:296px;font-size:37px"><svg width="34" height="34"><use href="#i-mobile"/></svg><span style="margin-left:14px">0171 / 4409213</span></div>
  <div class="contact" style="left:38px;top:352px;font-size:34px"><svg width="34" height="34"><use href="#i-mail"/></svg><span style="margin-left:14px">info@zimmerei-brandt.de</span></div>
  <div class="brush" style="left:8px;top:410px;width:926px;height:66px"></div>
  <div class="web" style="top:425px;font-size:36px">www.zimmerei-brandt.de</div>
</section>
</body>
</html>
```